Vitamin/Dietary Supplement Company needs a simple Hemp CBD Health retail website to display a few...

We need a simple website designed that will allow us to display a few products for purchase. We are a vitamin/dietary supplement company that wants to set up a separate website for CBD health products. CBD is a chemical compound found in hemp and cannabis plants that provide various health and medicinal benefits. Our target audience are individuals that suffer from health issues and would like to treat their pain relief with CBD as an alternative to prescription medication and over the counter drugs such as Paxorin and Dolvex. Looking for a simple and clean website that is easy for customers to navigate and purchase products.

Need extra days to review

Target Market(s)

Our target audience are individuals that suffer from health issues and would like to treat their pain relief with CBD as an alternative to prescription medication and over the counter drugs such as Paxorin and Dolvex.

Coding

Coded - Design and coding required

Font styles to use
Serif

Colors

Designer to choose colors to be used in the design.

Requirements
Nice to have
• Homepage, About page, FAQ page, Contact page, Blog page

```html
<!DOCTYPE html>
<html lang="en">
<head>
<meta charset="utf-8">
<title>Greenleaf Calm — CBD Health</title>
<link href="https://fonts.googleapis.com/css2?family=Poppins:wght@400;500;600;700&family=Roboto:wght@400;500;700&display=swap" rel="stylesheet">
<style>
  :root {
    --green: #55801f;
    --green-dark: #4a7219;
    --ink: #111111;
    --text: #222222;
    --muted: #8a8a8a;
    --panel: #f4f4f4;
    --line: #d9d9d9;
    --white: #ffffff;
  }
  * { box-sizing: border-box; margin: 0; padding: 0; }
  html, body { width: 1200px; height: 3448px; overflow: hidden; }
  body { position: relative; background: var(--white); font-family: "Roboto", sans-serif; color: var(--text); }
  .abs { position: absolute; }
  svg { display: block; }

  /* top bar */
  .topbar { left: 0; top: 0; width: 1200px; height: 53px; background: var(--green); color: var(--white); font-family: "Poppins", sans-serif; font-size: 14px; }
  .topbar .item { position: absolute; top: 17px; display: flex; align-items: center; gap: 6px; }
  .topbar .small { font-size: 12px; }

  /* header */
  .header { left: 0; top: 53px; width: 1200px; height: 137px; background: var(--white); }
  .brand { position: absolute; left: 90px; top: 40px; display: flex; align-items: center; gap: 18px; }
  .brand-dot { width: 56px; height: 56px; border-radius: 50%; background: var(--green); }
  .brand-name { font-family: "Poppins", sans-serif; font-weight: 700; font-size: 38px; color: var(--ink); letter-spacing: -0.5px; }
  .nav { position: absolute; left: 563px; top: 66px; display: flex; gap: 16px; font-family: "Poppins", sans-serif; font-weight: 600; font-size: 16.5px; color: var(--ink); }
  .nav .active { color: var(--green); }

  /* hero */
  .hero { left: 0; top: 190px; width: 1200px; height: 582px;
    background: radial-gradient(circle at 30% 60%, #8a7a62 0%, #5a5248 40%, #3c3a36 100%); }
  .hero-shade { position: absolute; inset: 0; background: rgba(0,0,0,0.25); }
  .hero h1 { position: absolute; left: 0; width: 1200px; top: 200px; text-align: center; font-family: "Poppins", sans-serif; font-weight: 700; font-size: 54px; color: var(--white); letter-spacing: -0.5px; }
  .hero p { position: absolute; left: 0; width: 1200px; top: 269px; text-align: center; font-size: 17.5px; color: var(--white); }
  .btn { display: flex; align-items: center; justify-content: center; background: var(--green); color: var(--white); border-radius: 30px; font-family: "Roboto", sans-serif; }
  .hero .btn { position: absolute; left: 523px; top: 318px; width: 157px; height: 49px; font-size: 16px; }

  /* about */
  .about { left: 0; top: 772px; width: 1200px; height: 515px; background: var(--panel); }
  .about-photo { position: absolute; left: 87px; top: 67px; width: 445px; height: 380px; background: linear-gradient(135deg, #7fd0dc 0%, #5fc1d1 50%, #e6c1b1 100%); box-shadow: 0 2px 6px rgba(0,0,0,0.25); }
  .about h2 { position: absolute; left: 568px; top: 88px; font-family: "Poppins", sans-serif; font-weight: 700; font-size: 36px; color: var(--ink); }
  .about h2 span { color: var(--green); }
  .about-text { position: absolute; left: 569px; top: 165px; width: 545px; font-size: 15.5px; line-height: 27px; color: var(--ink); }
  .about .btn { position: absolute; left: 566px; top: 363px; width: 155px; height: 48px; font-size: 16px; }

  /* products */
  .section-title { position: absolute; left: 0; width: 1200px; text-align: center; font-family: "Poppins", sans-serif; font-weight: 700; color: var(--green); }
  .products-title { top: 1353px; font-size: 36px; }
  .card { position: absolute; top: 1454px; width: 236px; height: 380px; background: var(--white); border: 1px solid #9c9c9c; box-shadow: 0 3px 6px rgba(0,0,0,0.25); }
  .card-photo { position: absolute; left: 2px; top: 2px; width: 230px; height: 230px; }
  .stars { position: absolute; left: 0; width: 100%; top: 229px; display: flex; justify-content: center; gap: 1px; }
  .card-name { position: absolute; left: 0; width: 100%; top: 262px; text-align: center; font-family: "Roboto", sans-serif; font-weight: 500; font-size: 14.5px; color: var(--ink); letter-spacing: 0.3px; }
  .card-price { position: absolute; left: 0; width: 100%; top: 285px; text-align: center; font-weight: 500; font-size: 15px; color: var(--ink); letter-spacing: 0.3px; }
  .card-actions { position: absolute; left: 0; bottom: 0; width: 100%; height: 53px; display: flex; border-top: 1px solid var(--line); background: linear-gradient(#f2f2f2, #ffffff 40%); }
  .card-actions div { flex: 1; display: flex; align-items: center; justify-content: center; border-right: 1px solid var(--line); }
  .card-actions div:last-child { border-right: none; }

  .dots { position: absolute; display: flex; gap: 7px; }
  .dot { border-radius: 50%; background: var(--green); }
  .dot.on { background: var(--ink); }

  /* testimonial */
  .quote-box { left: 268px; top: 2014px; width: 697px; height: 297px; background: var(--white); border: 1px solid #c8c8c8; box-shadow: 0 2px 5px rgba(0,0,0,0.15); }
  .quote-title { position: absolute; left: 0; width: 100%; top: 50px; text-align: center; font-family: "Poppins", sans-serif; font-weight: 500; font-size: 19px; color: var(--ink); }
  .quote-stars { position: absolute; left: 0; width: 100%; top: 92px; display: flex; justify-content: center; gap: 4px; }
  .quote-text { position: absolute; left: 100px; width: 497px; top: 149px; text-align: center; font-size: 15.5px; line-height: 20px; color: var(--text); }
  .avatar { left: 565px; top: 2251px; width: 100px; height: 100px; border-radius: 50%; background: radial-gradient(circle at 50% 40%, #a07a5c 0%, #5a4032 60%, #2b2422 100%); }
  .quote-name { left: 0; width: 1220px; top: 2370px; text-align: center; font-size: 16px; color: var(--text); }
  .arrow { width: 46px; height: 46px; border-radius: 50%; background: var(--ink); display: flex; align-items: center; justify-content: center; }

  /* features */
  .features { left: 0; top: 2473px; width: 1200px; height: 220px; background: var(--green); }
  .feature-icon { position: absolute; width: 108px; height: 108px; border-radius: 50%; background: var(--white); }
  .feature-label { position: absolute; font-family: "Poppins", sans-serif; font-weight: 600; font-size: 27px; line-height: 29px; color: var(--white); }

  /* newsletter */
  .newsletter-title { top: 2749px; font-size: 38px; letter-spacing: 0.5px; }
  .newsletter-text { left: 0; width: 1200px; top: 2817px; text-align: center; font-size: 15.5px; line-height: 22px; color: var(--ink); letter-spacing: 0.3px; }
  .field { left: 405px; top: 2881px; width: 388px; height: 30px; border: 1px solid #b5b5b5; background: var(--white); }
  .subscribe { left: 530px; top: 2930px; width: 140px; height: 39px; font-size: 16px; font-weight: 700; }

  /* footer */
  .footer { left: 0; top: 3009px; width: 1200px; height: 439px; background: var(--green); color: var(--white); }
  .footer h3 { position: absolute; font-family: "Poppins", sans-serif; font-weight: 700; font-size: 19px; letter-spacing: 0.2px; }
  .footer ul { position: absolute; list-style: none; font-size: 15.5px; }
  .footer li { height: 33px; }
  .address { position: absolute; left: 159px; top: 113px; font-size: 15.5px; line-height: 31px; }
  .address .row { display: flex; gap: 8px; }
  .copyright { position: absolute; left: 91px; top: 368px; font-family: "Poppins", sans-serif; font-weight: 600; font-size: 15.5px; }
  .social { position: absolute; left: 980px; top: 364px; display: flex; gap: 14px; }
  .social span { width: 26px; height: 26px; border-radius: 50%; background: var(--white); }
</style>
</head>
<body>

<svg width="0" height="0" style="position:absolute">
  <defs>
    <symbol id="star" viewBox="0 0 24 24"><polygon points="12,1.5 15,8.6 22.8,9.3 16.9,14.5 18.7,22.2 12,18.1 5.3,22.2 7.1,14.5 1.2,9.3 9,8.6"/></symbol>
    <symbol id="icon-cart" viewBox="0 0 24 24"><path d="M2 4h3l2.5 10h10l2-7H7" fill="none" stroke="currentColor" stroke-width="1.4"/><circle cx="9" cy="18" r="1.5" fill="none" stroke="currentColor" stroke-width="1.4"/><circle cx="16" cy="18" r="1.5" fill="none" stroke="currentColor" stroke-width="1.4"/></symbol>
    <symbol id="icon-heart" viewBox="0 0 24 24"><path d="M12 20s-7-4.5-7-10a4 4 0 0 1 7-2.5A4 4 0 0 1 19 10c0 5.5-7 10-7 10z" fill="none" stroke="currentColor" stroke-width="1.4"/></symbol>
    <symbol id="icon-swap" viewBox="0 0 24 24"><path d="M4 9h15l-3-3M20 15H5l3 3" fill="none" stroke="currentColor" stroke-width="1.4"/></symbol>
  </defs>
</svg>

<!-- top bar -->
<div class="abs topbar">
  <div class="item" style="left:95px">
    <svg width="12" height="12" viewBox="0 0 24 24"><path d="M6 2l4 5-2 3a12 12 0 0 0 6 6l3-2 5 4-3 4C10 21 3 14 2 5z" fill="#fff"/></svg>
    <span class="small">Hotline: 888-555-0142</span>
    <span style="margin:0 4px">|</span>
    <svg width="13" height="10" viewBox="0 0 26 20"><rect x="1" y="1" width="24" height="18" fill="none" stroke="#fff" stroke-width="2"/><path d="M1 1l12 10L25 1" fill="none" stroke="#fff" stroke-width="2"/></svg>
    <span>info@greenleafcalm.com</span>
  </div>
  <div class="item" style="left:930px">
    <svg width="16" height="16" viewBox="0 0 24 24"><circle cx="14" cy="10" r="7" fill="none" stroke="#fff" stroke-width="2.2"/><path d="M9 15l-6 6" stroke="#fff" stroke-width="2.4"/></svg>
    <span>Search</span>
    <span style="margin:0 2px">|</span>
    <svg width="20" height="18" viewBox="0 0 24 22"><use href="#icon-cart" color="#fff"/></svg>
    <span>Add Cart</span>
  </div>
</div>

<!-- header -->
<header class="abs header">
  <div class="brand">
    <div class="brand-dot"></div>
    <div class="brand-name">GREENLEAF CALM</div>
  </div>
  <nav class="nav">
    <span class="active">Home</span><span>Shop Now</span><span>About</span><span>Blog</span><span>Store Locator</span><span>Faq</span><span>Contact us</span>
  </nav>
</header>

<!-- hero -->
<section class="abs hero" role="img" aria-label="Photo of capsules, pills, supplement jars and a measuring tape on a wooden table">
  <div class="hero-shade"></div>
  <h1>WELCOME TO GREENLEAF CALM</h1>
  <p>Lorem Ipsum is simply dummy text of the printing and typesetting industry.</p>
  <div class="btn">SHOP NOW</div>
</section>

<!-- about -->
<section class="abs about">
  <div class="about-photo" role="img" aria-label="Photo of a hand holding a mix of capsules and pills against a light blue background"></div>
  <h2><span>ABOUT</span> US</h2>
  <p class="about-text">Lorem Ipsum is simply dummy text of the printing and typesetting industry. Lorem Ipsum has been the industry's standard dummy text ever since the 1500s, when an unknown printer took a galley of type and scrambled it to make a type specimen book.Lorem Ipsum is simply dummy text of the printing and typesetting industry. Lorem Ipsum has been the industry's standard dummy text ever.</p>
  <div class="btn">READ MORE</div>
</section>

<!-- products -->
<h2 class="section-title products-title">PRODUCTS</h2>

<div class="card" style="left:107px">
  <div class="card-photo" role="img" aria-label="Product photo of green hemp powder with capsules" style="background:radial-gradient(circle at 50% 55%, #a6b27a 0%, #d8dccb 45%, #ffffff 75%)"></div>
  <div class="stars" style="color:#fff"><svg width="16" height="16" style="stroke:#777;fill:none"><use href="#star"/></svg><svg width="16" height="16" style="stroke:#777;fill:none"><use href="#star"/></svg><svg width="16" height="16" style="stroke:#777;fill:none"><use href="#star"/></svg><svg width="16" height="16" style="stroke:#777;fill:none"><use href="#star"/></svg><svg width="16" height="16" style="stroke:#777;fill:none"><use href="#star"/></svg></div>
  <div class="card-name">CBD CALM TINCTURE 250MG</div>
  <div class="card-price">$145.00</div>
  <div class="card-actions"><div><svg width="18" height="18" color="#999"><use href="#icon-cart"/></svg></div><div><svg width="18" height="18" color="#999"><use href="#icon-heart"/></svg></div><div><svg width="18" height="18" color="#999"><use href="#icon-swap"/></svg></div></div>
</div>

<div class="card" style="left:360px">
  <div class="card-photo" role="img" aria-label="Product photo of a wooden bowl of capsules with a hemp leaf" style="background:radial-gradient(ellipse at 50% 55%, #b9b5a8 0%, #c58a5a 35%, #ffffff 70%)"></div>
  <div class="stars" style="fill:var(--green)"><svg width="19" height="19"><use href="#star"/></svg><svg width="19" height="19"><use href="#star"/></svg><svg width="19" height="19"><use href="#star"/></svg><svg width="19" height="19"><use href="#star"/></svg><svg width="19" height="19"><use href="#star"/></svg></div>
  <div class="card-name">CBD CALM TABLETS 250MG</div>
  <div class="card-price">$150.00</div>
  <div class="card-actions"><div><svg width="18" height="18" color="#999"><use href="#icon-cart"/></svg></div><div><svg width="18" height="18" color="#999"><use href="#icon-heart"/></svg></div><div><svg width="18" height="18" color="#999"><use href="#icon-swap"/></svg></div></div>
</div>

<div class="card" style="left:611px">
  <div class="card-photo" role="img" aria-label="Product photo of a green leaf with herbal capsules" style="background:radial-gradient(circle at 50% 45%, #4f8a2a 0%, #a9c98e 35%, #ffffff 70%)"></div>
  <div class="stars"><svg width="16" height="16" style="stroke:#777;fill:none"><use href="#star"/></svg><svg width="16" height="16" style="stroke:#777;fill:none"><use href="#star"/></svg><svg width="16" height="16" style="stroke:#777;fill:none"><use href="#star"/></svg><svg width="16" height="16" style="stroke:#777;fill:none"><use href="#star"/></svg><svg width="16" height="16" style="stroke:#777;fill:none"><use href="#star"/></svg></div>
  <div class="card-name">CBD CALM TINCTURE 250MG</div>
  <div class="card-price">$145.00</div>
  <div class="card-actions"><div><svg width="18" height="18" color="#999"><use href="#icon-cart"/></svg></div><div><svg width="18" height="18" color="#999"><use href="#icon-heart"/></svg></div><div><svg width="18" height="18" color="#999"><use href="#icon-swap"/></svg></div></div>
</div>

<div class="card" style="left:863px">
  <div class="card-photo" role="img" aria-label="Product photo of assorted supplement pills and capsules" style="background:radial-gradient(ellipse at 50% 45%, #b07a52 0%, #d9c3a8 40%, #ffffff 72%)"></div>
  <div class="stars" style="fill:var(--green)"><svg width="19" height="19"><use href="#star"/></svg><svg width="19" height="19"><use href="#star"/></svg><svg width="19" height="19"><use href="#star"/></svg><svg width="19" height="19"><use href="#star"/></svg><svg width="19" height="19"><use href="#star"/></svg></div>
  <div class="card-name">CBD CALM DROP 250MG</div>
  <div class="card-price">$145.00</div>
  <div class="card-actions"><div><svg width="18" height="18" color="#999"><use href="#icon-cart"/></svg></div><div><svg width="18" height="18" color="#999"><use href="#icon-heart"/></svg></div><div><svg width="18" height="18" color="#999"><use href="#icon-swap"/></svg></div></div>
</div>

<div class="dots" style="left:586px; top:1890px"><span class="dot" style="width:15px;height:15px"></span><span class="dot on" style="width:15px;height:15px"></span><span class="dot" style="width:15px;height:15px"></span></div>

<!-- testimonial -->
<div class="abs arrow" style="left:175px; top:2138px"><svg width="20" height="20" viewBox="0 0 20 20"><path d="M13 3l-7 7 7 7" fill="none" stroke="#fff" stroke-width="3"/></svg></div>
<div class="abs arrow" style="left:1006px; top:2139px"><svg width="20" height="20" viewBox="0 0 20 20"><path d="M7 3l7 7-7 7" fill="none" stroke="#fff" stroke-width="3"/></svg></div>

<div class="abs quote-box">
  <div class="quote-title">"Very good but not exceptional"</div>
  <div class="quote-stars" style="fill:var(--green)"><svg width="23" height="23"><use href="#star"/></svg><svg width="23" height="23"><use href="#star"/></svg><svg width="23" height="23"><use href="#star"/></svg><svg width="23" height="23"><use href="#star"/></svg><svg width="23" height="23"><use href="#star"/></svg></div>
  <p class="quote-text">Lorem ipsum dolor sit amet, ultrices odio vitae a est, justo fusce commodo at, pellentesque pharetra. Donec mi elit hendrerit felis non, at sodalestnon.</p>
</div>
<div class="abs avatar" role="img" aria-label="Customer portrait photo"></div>
<div class="abs quote-name">-Elias</div>
<div class="dots" style="left:594px; top:2405px; gap:3px"><span class="dot on" style="width:9px;height:9px"></span><span class="dot" style="width:9px;height:9px"></span><span class="dot on" style="width:9px;height:9px"></span></div>

<!-- features -->
<section class="abs features">
  <div class="feature-icon" style="left:132px; top:57px" role="img" aria-label="Free delivery truck icon"></div>
  <div class="feature-label" style="left:256px; top:84px">Wordwide<br>Delivery</div>
  <div class="feature-icon" style="left:461px; top:55px" role="img" aria-label="Secure payment handshake icon"></div>
  <div class="feature-label" style="left:581px; top:84px">Safe<br>Payments</div>
  <div class="feature-icon" style="left:806px; top:55px" role="img" aria-label="Support agent icon"></div>
  <div class="feature-label" style="left:937px; top:84px; text-align:center">24/7 Help<br>Center</div>
</section>

<!-- newsletter -->
<h2 class="section-title newsletter-title">Newsletter</h2>
<p class="abs newsletter-text">Sign up to our newsletter and be the first to hear the latest offers, events, news and<br>updates from Greenleaf Calm .Read our privacy policy here.</p>
<div class="abs field"></div>
<div class="abs btn subscribe">Subscribe</div>

<!-- footer -->
<footer class="abs footer">
  <h3 style="left:159px; top:80px">CBD SHOP</h3>
  <div class="address">
    <div class="row"><svg width="14" height="18" viewBox="0 0 14 20" style="margin-top:6px"><path d="M7 0a7 7 0 0 0-7 7c0 5 7 13 7 13s7-8 7-13a7 7 0 0 0-7-7z" fill="#fff"/><circle cx="7" cy="7" r="2.5" fill="#55801f"/></svg><span>4820 Cedar Grove<br>Ave. North Vale,<br>CA 90010</span></div>
    <div class="row" style="margin-top:2px"><svg width="14" height="14" viewBox="0 0 24 24" style="margin-top:9px"><path d="M6 2l4 5-2 3a12 12 0 0 0 6 6l3-2 5 4-3 4C10 21 3 14 2 5z" fill="#fff"/></svg><span>(818) 555-0173</span></div>
  </div>

  <h3 style="left:444px; top:77px">HELP</h3>
  <ul style="left:446px; top:118px"><li>Delivery</li><li>Returns</li><li>Contact</li><li>FAQs</li><li>CSR policy</li><li>Size Guide</li></ul>

  <h3 style="left:655px; top:78px">LINK</h3>
  <ul style="left:656px; top:118px"><li>Home</li><li>Shop Now</li><li>About</li><li>Blog</li><li>Store Locator</li><li>Faq</li><li>Contact us</li></ul>

  <h3 style="left:835px; top:75px">CUSTOMER SERVICE</h3>
  <ul style="left:839px; top:118px"><li>Contact</li><li>Site map</li><li>Gift certificates</li></ul>

  <div class="copyright">© Copyright 2018 – GREENLEAF CALM</div>
  <div class="social" aria-label="Social links"><span></span><span></span><span></span><span></span></div>
</footer>

</body>
</html>
```